LineUp Banner for EDM music Festival!

Hello,

i need a lineup banner for an edm festival.

It should looks similar to the lineup banner uploaded here. I also added the background image.

Feel free to add something you think it looks cool.
Background have to be used. I would need after your work is done the psd file, so I can edit the text / names by myself.

Size should be around 2000x3000.

Thank you

Industry/Entity Type

Festival

Requirements
Must have
• Similar to the lineup banner. Feel free to add something you think it looks cool.
• Background have to be used.
Nice to have
• In best case it will be as most similar as the uploaded lineup banner.

```html
<!DOCTYPE html>
<html lang="en">
<head>
<meta charset="utf-8">
<title>AAA Festival – Lineup Poster</title>
<link rel="stylesheet" href="https://fonts.googleapis.com/css2?family=Audiowide&family=Montserrat:wght@400;700&family=Poiret+One&family=Saira+Condensed:wght@400;500;600&display=swap">
<style>
  :root {
    --page-bg: #ffffff;
    --night: #0b0810;
    --violet: #4a1d4f;
    --magenta: #7a2a6a;
    --amber: #f2b21c;
    --gold: #e9a92a;
    --flare: #fff6c8;
    --orange: #e8621a;
    --ink: #0a0a0a;
    --white: #ffffff;
    --band: rgba(20, 18, 22, 0.72);
  }
  * { margin: 0; padding: 0; box-sizing: border-box; }
  html, body {
    width: 865px;
    height: 1200px;
    overflow: hidden;
    background: var(--page-bg);
  }
  .poster {
    position: absolute;
    left: 86px;
    top: 82px;
    width: 694px;
    height: 1040px;
    overflow: hidden;
    background: var(--night);
    color: var(--white);
  }
  .crowd-photo {
    position: absolute;
    inset: 0;
    background:
      radial-gradient(ellipse 260px 200px at 62% 44%, rgba(255, 246, 200, 0.95), rgba(242, 178, 28, 0.55) 45%, rgba(242, 178, 28, 0) 75%),
      radial-gradient(ellipse 220px 160px at 88% 22%, rgba(255, 255, 255, 0.85), rgba(255, 255, 255, 0) 70%),
      radial-gradient(ellipse 300px 220px at 20% 30%, rgba(122, 42, 106, 0.8), rgba(122, 42, 106, 0) 70%),
      radial-gradient(ellipse 380px 260px at 50% 62%, rgba(150, 95, 60, 0.55), rgba(150, 95, 60, 0) 75%),
      linear-gradient(180deg, var(--violet) 0%, #3a2030 35%, #2a1a1c 60%, #120d12 80%, var(--night) 100%);
  }
  .light-streak {
    position: absolute;
    left: 360px;
    top: 460px;
    width: 4px;
    height: 420px;
    background: linear-gradient(180deg, rgba(255,255,255,0), rgba(220,235,255,0.7), rgba(255,255,255,0));
    transform: rotate(32deg);
  }
  .light-streak.second { left: 560px; top: 470px; height: 320px; }
  .top-band {
    position: absolute;
    left: 0; top: 27px;
    width: 100%; height: 46px;
    background: var(--band);
    display: flex;
    align-items: center;
    justify-content: center;
    gap: 8px;
    font-family: "Montserrat", sans-serif;
    font-size: 22px;
    letter-spacing: 1px;
    white-space: nowrap;
  }
  .top-band .presenter { font-weight: 700; }
  .top-band .presents { font-weight: 400; }
  .festival-title {
    position: absolute;
    left: 51px; top: 100px;
    width: 592px;
    text-align: center;
    white-space: nowrap;
    font-family: "Audiowide", sans-serif;
    font-weight: 400;
    font-size: 62px;
    line-height: 62px;
    letter-spacing: 1px;
    transform: scaleY(1.35);
    transform-origin: center top;
    background: linear-gradient(180deg, var(--flare) 0%, var(--amber) 45%, var(--orange) 100%);
    -webkit-background-clip: text;
    background-clip: text;
    color: transparent;
  }
  .rule {
    position: absolute;
    left: 51px;
    width: 592px;
    height: 3px;
    background: var(--flare);
  }
  .rule.upper { top: 195px; }
  .rule.lower { top: 267px; }
  .event-date {
    position: absolute;
    left: 51px; top: 202px;
    width: 592px;
    text-align: center;
    white-space: nowrap;
    font-family: "Poiret One", sans-serif;
    font-size: 64px;
    line-height: 64px;
    background: linear-gradient(90deg, var(--gold) 0%, var(--flare) 60%, var(--white) 100%);
    -webkit-background-clip: text;
    background-clip: text;
    color: transparent;
  }
  .lineup {
    position: absolute;
    left: 51px; top: 292px;
    width: 600px;
    display: grid;
    grid-template-columns: 315px 285px;
    font-family: "Saira Condensed", sans-serif;
    font-weight: 500;
    font-size: 48px;
    line-height: 54px;
    white-space: nowrap;
    color: var(--ink);
    list-style: none;
  }
  .general-info {
    position: absolute;
    left: 0; top: 768px;
    width: 100%;
    text-align: center;
    white-space: nowrap;
    font-family: "Saira Condensed", sans-serif;
  }
  .general-info h2 {
    font-weight: 500;
    font-size: 28px;
    line-height: 32px;
    margin-bottom: 12px;
  }
  .general-info p {
    font-weight: 500;
    font-size: 22px;
    line-height: 28px;
  }
  .sponsors {
    position: absolute;
    left: 51px; top: 938px;
    width: 592px; height: 66px;
    border: 2px solid var(--gold);
    border-radius: 10px;
  }
  .sponsors-label {
    position: absolute;
    left: 50%; top: -9px;
    transform: translateX(-50%);
    padding: 0 5px;
    background: var(--night);
    font-family: "Saira Condensed", sans-serif;
    font-size: 13px;
    line-height: 16px;
    color: var(--gold);
  }
  .sponsor-slots {
    position: absolute;
    left: 25px; top: 12px;
    display: flex;
    gap: 26px;
    list-style: none;
  }
  .sponsor-slot {
    width: 44px; height: 38px;
    background: var(--white);
  }
</style>
</head>
<body>
  <main class="poster">
    <div class="crowd-photo" role="img" aria-label="Festival crowd with raised hands under bright yellow and violet stage lights"></div>
    <div class="light-streak"></div>
    <div class="light-streak second"></div>

    <header class="top-band"><span class="presenter">AAA</span><span class="presents">PRESENT</span></header>
    <h1 class="festival-title">AAA FESTIVAL</h1>
    <div class="rule upper"></div>
    <p class="event-date">OCTOBER 31 SUNDAY</p>
    <div class="rule lower"></div>

    <ul class="lineup">
      <li>DJ ARTIST NAME</li>
      <li>DJ ARTIST NAME</li>
      <li>DJ ARTIST NAME</li>
      <li>DJ ARTIST NAME</li>
    </ul>

    <section class="general-info">
      <h2>GENERAL INFORMATION</h2>
      <p>GENERAL INFORMATION ▪ GENERAL INFORMATION ▪ GENERAL INFORMATION</p>
      <p>GENERAL INFORMATION ▪ GENERAL INFORMATION ▪ GENERAL INFORMATION</p>
      <p>GENERAL INFORMATION ▪ GENERAL INFORMATION ▪ GENERAL INFORMATION</p>
    </section>

    <section class="sponsors">
      <span class="sponsors-label">SPONSORS</span>
      <ul class="sponsor-slots">
        <li class="sponsor-slot"></li>
        <li class="sponsor-slot"></li>
        <li class="sponsor-slot"></li>
        <li class="sponsor-slot"></li>
        <li class="sponsor-slot"></li>
        <li class="sponsor-slot"></li>
        <li class="sponsor-slot"></li>
        <li class="sponsor-slot"></li>
      </ul>
    </section>
  </main>
</body>
</html>
```